The 5 stages of grief experience

I'm an artist and I'm launching my art debut and i need a whole set of thing. I have the logo and the colors and the list of what I need:
Sponsorship proposal (I have the info to be pasted once design is ready)
Flyer for my art. It's about the 5 stages of grief and its like you go into a maze to go through each art instillation that takes you over each feeling, there is a lot of feelings and symmetry in the art.
Denial
Anger
Depression
Bargaining
Acceptance
Updates

We are rushing on this project if anyone is interested we need it asap Added Monday, March 6, 2017

Target Market(s)

Visual Art society

Font styles to use
Sans Serif

Colors
fee4d6
f8ba93
000000
5c5c5c
fbfbfb

Requirements
Must have
• Symmetry
• Feeling
• Strong message
• Bold
• An artistic idea I like a lot is a black and white moon changes and it's 5 different moons starting from a crescent ending in a full moon all next to each other or on top of each other and the phases underneath in small geometric font
Nice to have
• Softness
Should not have
• Femininity

```html
<!DOCTYPE html>
<html lang="en">
<head>
<meta charset="utf-8">
<title>LUMA Arts Event – Sponsorship Proposal</title>
<link rel="stylesheet" href="https://fonts.googleapis.com/css2?family=Open+Sans:wght@400;700;800&display=swap">
<style>
  :root {
    --peach: #fee4d6;
    --apricot: #f8ba93;
    --ink: #000000;
    --slate: #5c5c5c;
    --paper: #fbfbfb;
    --stage: #e4e4e4;
  }
  * { box-sizing: border-box; margin: 0; padding: 0; }
  html, body { width: 1200px; height: 858px; overflow: hidden; }
  body {
    background: var(--stage);
    font-family: "Open Sans", Arial, sans-serif;
    color: var(--ink);
    position: relative;
  }
  .sheet {
    position: absolute;
    top: 29px;
    width: 560px;
    height: 800px;
    background: var(--peach);
    border: 3px solid var(--ink);
    overflow: hidden;
  }
  .sheet--overview { left: 30px; }
  .sheet--tiers { left: 610px; }
  .abs { position: absolute; }
  ul { list-style: none; }
  li { position: relative; padding-left: 10px; }
  li::before { content: "•"; position: absolute; left: 0; }
  .small { font-size: 9.5px; line-height: 1.3; }

  /* overview sheet */
  .brand-mark { left: 18px; top: 18px; width: 104px; text-align: center; }
  .brand-mark .disc { width: 96px; height: 96px; border-radius: 50%; background: var(--ink); margin: 0 auto; }
  .brand-mark .name { font-size: 17px; font-weight: 400; letter-spacing: 2px; margin-top: 2px; }
  .masthead { left: 145px; top: 16px; }
  .masthead h1 { font-size: 36px; font-weight: 800; line-height: 1.05; }
  .masthead .dates { font-size: 27px; line-height: 1.1; }
  .masthead .venue { font-size: 27px; font-weight: 800; line-height: 1.1; }
  .intro { left: 140px; top: 142px; width: 400px; font-size: 10px; line-height: 1.35; }
  .tab { background: var(--ink); color: var(--paper); font-weight: 700; font-size: 12px; padding: 3px 12px; border-radius: 0 12px 12px 0; }
  .tab--experience { left: 0; top: 208px; width: 230px; }
  .win { left: 14px; top: 232px; width: 520px; }
  .win h2 { font-size: 14px; font-weight: 400; }
  .feature-band { left: 0; top: 318px; }
  .about { left: 296px; top: 326px; width: 248px; color: var(--paper); font-size: 9px; }
  .about h3, .fit h3 { font-size: 12px; font-weight: 700; margin-bottom: 3px; }
  .about li { margin-bottom: 3px; }
  .fit { left: 46px; top: 394px; width: 180px; color: var(--paper); }
  .fit li { margin-bottom: 4px; }
  .interested {
    left: 150px; top: 624px; width: 390px; height: 164px;
    background: var(--ink); color: var(--paper);
    border-radius: 26px; padding: 12px 22px; text-align: center;
  }
  .interested h3 { font-size: 14px; font-weight: 700; margin-bottom: 5px; }
  .interested p { font-size: 9.5px; line-height: 1.32; margin-bottom: 3px; }

  /* tiers sheet */
  .tiers-title { left: 0; top: 0; width: 554px; height: 62px; padding: 12px 0 0 36px; font-size: 29px; font-weight: 800; }
  .tier-head { background: var(--ink); color: var(--paper); font-weight: 700; font-size: 11px; padding: 4px 8px; }
  .tier-body { background: var(--slate); color: var(--paper); padding: 4px 8px 5px; }
  .tier-body h4 { font-size: 10px; font-weight: 700; margin-top: 1px; }
  .tier-body li { margin-bottom: 1px; }
  .tier--presenting { left: 10px; top: 66px; width: 206px; }
  .tier--presenting .tier-body { height: 470px; }
  .tier--presenting .tier-body li { margin-bottom: 3px; }
  .tier-stack { left: 224px; top: 66px; width: 320px; }
  .tier-stack .tier { margin-bottom: 7px; }
  .contact-block { left: 10px; top: 548px; width: 206px; text-align: center; }
  .contact-block .disc { width: 58px; height: 58px; border-radius: 50%; background: var(--ink); margin: 0 auto; }
  .contact-block .name { font-size: 12px; letter-spacing: 2px; }
  .contact-block .lines { font-size: 11px; font-weight: 700; margin-top: 4px; line-height: 1.3; }
  .save-date {
    left: 0; top: 668px; width: 554px; height: 126px;
    background: var(--ink); color: var(--paper);
    text-align: center; padding: 12px 30px 0 230px;
  }
  .save-date h3 { font-size: 13px; font-weight: 700; margin-bottom: 4px; }
  .save-date p { font-size: 9.5px; line-height: 1.4; }
</style>
</head>
<body>

<section class="sheet sheet--overview">
  <div class="abs brand-mark">
    <div class="disc"></div>
    <div class="name">LUMA</div>
  </div>
  <header class="abs masthead">
    <h1>LUMA Arts Event</h1>
    <div class="dates">April 12.13.14</div>
    <div class="venue">Sahra Art Gallery</div>
  </header>

  <p class="abs intro">Sponsoring LUMA Arts Event provides you the unique opportunity to connect with the art community in Saudi Arabia, to build brand awareness and show your company's support of an important cause: the arts!</p>

  <div class="abs tab tab--experience">Experience the art ...</div>

  <div class="abs win small">
    <h2>It's a win-win</h2>
    <ul>
      <li>Sponsoring LUMA Arts Event provides you the unique opportunity to connect with the art community in Saudi Arabia, to build brand awareness and show your company's support of an important cause: the arts!</li>
      <li>This event reaches a certain key audience segment and provides a fun, entertaining and inspiring way for you to help us reach the audience, VIPs and volunteers. Feel good about supporting our local arts, heritage and cultural organisations as you enjoy an unforgettable evening.</li>
    </ul>
  </div>

  <svg class="abs feature-band" width="554" height="320" viewBox="0 0 554 320" aria-hidden="true">
    <rect x="0" y="0" width="554" height="272" fill="var(--slate)"/>
    <circle cx="132" cy="160" r="156" fill="var(--peach)"/>
    <circle cx="132" cy="160" r="140" fill="var(--slate)"/>
  </svg>

  <div class="abs about small">
    <h3>About the event</h3>
    <ul>
      <li>Being the top events of the year, art exhibitions and galleries are highly requested in Saudi. Hence, an event with two different types of artists decided to collaborate to host for the first time an interactive art event for the very first time in Saudi. Artists Reem AlSaadi and Fahad AlMutairi are the founders of the LUMA Arts Event and aim to portray art in a unique view to Saudi's art audience.</li>
      <li>Targeting all art enthusiasts, we allow them to enjoy the arts while being a part of it, and get the chance to enjoy various art pieces that carry meaning about human emotions and social experiences. Furthermore, people that attend LUMA Arts Event will get the opportunity to enjoy the arts while enjoying good food, drinks, and mingle with Saudi's finest art community.</li>
    </ul>
  </div>

  <div class="abs fit small">
    <h3>Find your fit</h3>
    <ul>
      <li>Looking for the opportunity to become apart of one the most unique events of the year, to put your company name in front of hundreds of sophisticated attendees.</li>
      <li>Want to show your employees and investors a dedication to our community.</li>
      <li>Consider a sponsorship at LUMA Arts Event</li>
    </ul>
  </div>

  <div class="abs interested">
    <h3>Interested?</h3>
    <p>LUMA Arts Event is really excited to present art in a unique way. For the first time in Saudi you get to "experience the art" and be part of it.</p>
    <p>Kindly find attached the event's Sponsorship form agreement with all the 5 categories to choose from in the same email sent to you.</p>
    <p>For any further inquiries, please feel free to contact us at +966 500 000 000 anytime after 12 pm.</p>
    <p>Or email us on hello@lumaarts.example</p>
  </div>
</section>

<section class="sheet sheet--tiers">
  <h2 class="abs tiers-title">Sponsorship opportunities</h2>

  <article class="abs tier tier--presenting small">
    <div class="tier-head">1. Presenting Sponsor: 25,000 SR</div>
    <div class="tier-body">
      <h4>Benefits:</h4>
      <ul>
        <li>Prominent sponsor recognition on all event related marketing: save the date, invitations, flyers, and posters.</li>
        <li>Sponsor listing at the event and on social media outlets regarding the event.</li>
        <li>Sponsor recognition and link from the event page on LUMAEvents social page.</li>
      </ul>
      <h4>Unique benefits:</h4>
      <ul>
        <li>Company name mentioned in all media advertising print and online.</li>
        <li>Sponsor advertisement in event program</li>
        <li>10 tickets to the exclusive VIP opening (invitees only) of the event</li>
        <li>Opportunity to interact with VIP influencers and invitees (ambassadors, company owners, bloggers, etc.)</li>
        <li>Sponsor table at the event and the opportunity to display any products, services, or company materials (to an extent that does not disobey the rules and regulations of the event)</li>
      </ul>
    </div>
  </article>

  <div class="abs tier-stack small">
    <article class="tier">
      <div class="tier-head">2. Supporting sponsor: 10,000 SR</div>
      <div class="tier-body">
        <h4>Benefits:</h4>
        <ul>
          <li>Prominent sponsor recognition on all event related marketing: save the date, invitations, flyers, and posters.</li>
          <li>Sponsor listing at the event and on social media outlets regarding the event.</li>
          <li>Sponsor recognition and link from the event page on LUMAEvents social page.</li>
        </ul>
        <h4>Unique benefits:</h4>
        <ul><li>6 tickets to the exclusive VIP opening (invitees only) of the event</li></ul>
      </div>
    </article>
    <article class="tier">
      <div class="tier-head">3. Regular sponsor: 5,000 SR</div>
      <div class="tier-body">
        <h4>Benefits:</h4>
        <ul>
          <li>Sponsor listing at the event and on social media outlets regarding the event.</li>
          <li>Sponsor recognition and link from the event page on LUMAEvents social page.</li>
        </ul>
        <h4>Unique benefits:</h4>
        <ul><li>2 tickets to the exclusive VIP opening (invitees only) of the event</li></ul>
      </div>
    </article>
    <article class="tier">
      <div class="tier-head">4. Catering sponsor: 3,000 SR</div>
      <div class="tier-body">
        <h4>Benefits:</h4>
        <ul>
          <li>Sponsor listing at the event and on social media outlets regarding the event.</li>
          <li>Sponsor recognition and link from the event page on LUMAEvents social page.</li>
        </ul>
      </div>
    </article>
    <article class="tier">
      <div class="tier-head">5. Social Media sponsor</div>
      <div class="tier-body">
        <h4>Benefits:</h4>
        <ul>
          <li>Sponsor listing at the event and on social media outlets regarding the event.</li>
          <li>Sponsor recognition and link from the event page on LUMAEvents social page.</li>
        </ul>
        <h4>Unique benefits:</h4>
        <ul>
          <li>2 tickets to the exclusive VIP opening (invitees only) of the event</li>
          <li>Free entry access to the full duration of the event</li>
        </ul>
      </div>
    </article>
  </div>

  <div class="abs contact-block">
    <div class="disc"></div>
    <div class="name">LUMA</div>
    <div class="lines">hello@lumaarts.example<br>+966 500 000 000</div>
  </div>

  <div class="abs save-date">
    <h3>Save the date!</h3>
    <p>VIP tickets for the opening of LUMA Arts Event on April 12, 2017.<br>
    The events opens its doors for everyone on April 12, 13, and 14.<br>
    We hope to see you there!<br>
    Best,<br>
    LUMA Arts Event Team</p>
  </div>
</section>

</body>
</html>
```